Business Card Design for Property Investment Company

We need a new business card designed that reflects our new domain. and also reflects more closely the style and branding of our website www.kpmholdings.co.uk

The template will be the same for two different directors. Logo and images from website, as well as more detail on brief are attached

Want a two-side design
Details from above image need to change as follows:
E: glen.marsh@kpmholdings.co.uk
W: www.kpmholdings.co.uk

Also, need second card, same design, for:
Simon Marsh
Director
M: +44 (0)7812 364197
E: simon.marsh@kpmholdings.co.uk
A: same as above
W: same as above

Attached are a selection of images from the website that could be used on the website, as well as the logo

Target Market(s)

Property/Real-estate professionals, invesroea and developers

Industry/Entity Type

Real Estate Development

Contact Information for Business Card

see brief attachment

Font styles to use
Sans Serif

Requirements
Must have
• Contact info as per brief
• Look and feel of the website - www.kpmholdings.co.uk
• (a selection of images that can be used have been attached, along with logo)
• Slick and professional look
Nice to have
• maybe include an image on one side of the card with logo, and contact info on the other (only a suggestion)
Should not have
• anything gimmicky

```html
<!DOCTYPE html>
<html lang="en">
<head>
<meta charset="utf-8">
<title>KPM Holdings – Business Card</title>
<link href="https://fonts.googleapis.com/css2?family=Jost:wght@400;600;700&display=swap" rel="stylesheet">
<style>
  :root {
    --backdrop: #a2a2a2;
    --card-white: #ffffff;
    --brand-green: #0a3020;
    --photo-dark: #3a2a22;
    --photo-mid: #5a4234;
    --paper: #e9dcc2;
  }
  html, body {
    margin: 0;
    padding: 0;
    width: 1189px;
    height: 1200px;
    overflow: hidden;
    background: var(--backdrop);
    font-family: "Jost", Arial, sans-serif;
  }
  .canvas { position: relative; width: 1189px; height: 1200px; }
  .card {
    position: absolute;
    top: 162px;
    width: 516px;
    height: 905px;
    border-radius: 25px;
    overflow: hidden;
    box-shadow: 0 2px 6px rgba(0,0,0,0.25);
  }
  .card--front { left: 54px; background: var(--card-white); color: var(--brand-green); }
  .card--back { left: 598px; }

  .brand {
    position: absolute;
    display: flex;
    align-items: center;
    gap: 12px;
    font-weight: 600;
    font-size: 34px;
    line-height: 1;
    white-space: nowrap;
  }
  .brand__dot { width: 30px; height: 30px; border-radius: 50%; background: currentColor; flex: none; }
  .card--front .brand { left: 0; right: 0; justify-content: center; top: 186px; color: var(--brand-green); }
  .card--back .brand { right: 44px; top: 190px; color: var(--card-white); }

  .holder { position: absolute; left: 56px; top: 552px; line-height: 1; }
  .holder__name { font-size: 34px; font-weight: 600; margin: 0; }
  .holder__role { font-size: 21px; font-weight: 400; margin: 2px 0 0; }

  .address { position: absolute; left: 56px; top: 650px; font-size: 22px; line-height: 30px; margin: 0; }

  .contacts { position: absolute; left: 56px; top: 724px; font-size: 22px; line-height: 30.5px; margin: 0; padding: 0; list-style: none; }
  .contacts b { font-weight: 700; display: inline-block; width: 40px; }

  .photo {
    position: absolute; inset: 0;
    background: linear-gradient(165deg, var(--photo-dark) 0%, var(--photo-mid) 38%, var(--paper) 75%, #f3ece0 100%);
  }
</style>
</head>
<body>
<div class="canvas">
  <section class="card card--front">
    <div class="brand"><span class="brand__dot"></span>KPM Holdings</div>
    <div class="holder">
      <h1 class="holder__name">Glen Marsh</h1>
      <p class="holder__role">Director</p>
    </div>
    <p class="address">12 Elmstead Lane<br>Bickley, Kent, BR1 2QT</p>
    <ul class="contacts">
      <li><b>M:</b>+44 (0)7700 418273</li>
      <li><b>E:</b>glen.marsh@kpmholdings.co.uk</li>
      <li><b>W:</b>www.kpmholdings.co.uk</li>
    </ul>
  </section>

  <section class="card card--back">
    <div class="photo" role="img" aria-label="Photo of a coffee cup and an open lined notebook on a dark wooden desk"></div>
    <div class="brand"><span class="brand__dot"></span>KPM Holdings</div>
  </section>
</div>
</body>
</html>
```